■依頼の概要
子どもの結婚を望む親御様に向けた電子書籍(pagora出版)の表紙デザイン作成をお願いします。
電子書籍なので、タイトルがはっきり分かるものでお願いします。

■本のタイトル
いつか、わが家にも春は来るだろうか? ~家族の未来をひらく手引き~

■本の内容
子どもの結婚を望む親御様に向けて、今どきの婚活・結婚事情をデータでご紹介している他、婚活成幸するための考え方や事例を紹介しています。
原稿内容を添付します。

■読者ターゲット
息子・娘に結婚してほしいと願っている親御様
(20代~50代位の独身のお子さんに結婚してほしいと願っている親御様・子どもの結婚のためなら何でもする覚悟の親御様・親子関係が良好ではない親御様)

■デザイン要望
原稿内容を参考にしていただいて、より売れることを目的としたデザインにしてください。
デザイナーさんのパフォーマンスを引き出したいので、デザイナーさんのセンスにお任せします。

■その他
Zuvomiの利用が不慣れなためアクション方法が分からず、対応がスマートでない場合はご指摘・ご教示いただけますと助かります。
何かご不明な点がございましたら、お気軽にご質問ください。
尚、最終的には私が籍を置く出版スクール内での投票で、一番人気のあったデザインに決めさせていただきます。

以上、何卒宜しくお願い申し上げます。
【ご提案をいただいた皆様へ】

この度はステキな表紙デザインを数多くご提案いただきまして、本当にありがとうございます。
皆様からいただきましたご提案は、私が籍を置く出版スクール内でのルールで、デザインの人気投票を行い一番得票数の多かったデザインを採用させていただきます。
それ故、締め切り後しばらくお時間をいただきますが、表紙をお願いしたい方には後日ご連絡をさせていただきます。
尚、全員の方お一人お一人にお礼のご挨拶ができませんことお許しいただき、この場でのご挨拶とさせていただきます。
この度の皆様からのご提案に心から感謝申し上げます。
ありがとうございましたm(__)m

皆様からご提案をいただきまして、私が籍を置く出版スクール内で表紙デザインの人気投票を行いました(これが、出版スクールでの標準的ルールになっています)
そうしましたところ、こちらのデザインに一番票が集まりました。
ご投票いただいた方々のコメントには、親の気持ちがそのままデザインに表されている・タイトルがスッと目に入ってきた・優しいピンクが、焦燥感を和らげてる・水引に縁起の良さを感じるなどたくさんのコメントをいただきました。

この度は、皆様からたくさんのご提案をいただきまして、本当にありがとうございましたm(__)m
素晴らしい作品に恵まれ、また私の好みをお伝えさせていただいた際には、皆様快く修正や追加提案をいただいて、また迅速にご対応いただいて、本当に有難く感謝の気持ちでいっぱいでおります。
これだけたくさんの、しかも素晴らしいご提案をいただいたら私自身もどれにしようか悩んでしまいました。
最終的には、人気投票で一番人気のデザインに決めさせていただきました。
この度のコンペにご参加の全ての皆様に心から感謝申し上げます。

```html
<!DOCTYPE html>
<html lang="ja">
<head>
<meta charset="UTF-8">
<title>いつか、わが家にも春は来るだろうか?</title>
<link href="https://fonts.googleapis.com/css2?family=Shippori+Mincho+B1:wght@500;700;800&family=Noto+Sans+JP:wght@500;700&display=swap" rel="stylesheet">
<style>
  :root {
    --paper: #ffffff;
    --ink: #1f2a44;
    --bloom-deep: #2f7fc6;
    --bloom-mid: #5ab6ea;
    --bloom-light: #bfe6f7;
    --leaf: #7fa86a;
    --accent: #e23c7f;
  }
  * { margin: 0; padding: 0; box-sizing: border-box; }
  html, body { width: 750px; height: 1200px; overflow: hidden; background: var(--paper); }
  .cover {
    position: relative;
    width: 750px; height: 1200px;
    background: var(--paper);
    font-family: "Shippori Mincho B1", serif;
    color: var(--ink);
    overflow: hidden;
  }
  .flower-border { position: absolute; inset: 0; width: 750px; height: 1200px; }
  .subtitle {
    position: absolute; top: 95px; left: 0; width: 750px;
    text-align: center; font-size: 29px; font-weight: 700; letter-spacing: 2px;
  }
  .title {
    position: absolute; top: 165px; left: 0; width: 750px;
    text-align: center; font-size: 60px; font-weight: 800; line-height: 1.35;
    letter-spacing: 1px;
  }
  .author { position: absolute; top: 510px; left: 405px; }
  .author-role { font-size: 18px; font-weight: 700; letter-spacing: 1px; }
  .author-name { margin-top: 10px; font-size: 38px; font-weight: 800; letter-spacing: 4px; }
  .author-name small { font-size: 16px; font-weight: 500; letter-spacing: 0; margin-left: 4px; }
  .message {
    position: absolute; top: 690px; left: 405px; width: 280px;
    font-size: 24px; font-weight: 700; line-height: 1.62;
  }
  .gift { position: absolute; top: 935px; left: 38px; width: 205px; }
  .gift-label {
    display: inline-block; background: var(--accent); color: #fff;
    font-family: "Noto Sans JP", sans-serif; font-weight: 700;
    font-size: 22px; padding: 4px 10px; letter-spacing: 1px;
  }
  .gift-body {
    background: var(--paper); border: 3px solid var(--accent);
    padding: 10px 12px; font-size: 26px; font-weight: 800; line-height: 1.35;
  }
</style>
</head>
<body>
<div class="cover">
  <svg class="flower-border" viewBox="0 0 750 1200" role="img" aria-label="青い勿忘草の花が上部と左右を縁取る装飾">
    <defs>
      <linearGradient id="bloom" x1="0" y1="0" x2="1" y2="1">
        <stop offset="0" stop-color="var(--bloom-light)"/>
        <stop offset="0.5" stop-color="var(--bloom-mid)"/>
        <stop offset="1" stop-color="var(--bloom-deep)"/>
      </linearGradient>
      <filter id="soft" x="-20%" y="-20%" width="140%" height="140%">
        <feGaussianBlur stdDeviation="14"/>
      </filter>
    </defs>
    <g filter="url(#soft)" fill="url(#bloom)">
      <rect x="-40" y="-40" width="830" height="95"/>
      <rect x="-40" y="-40" width="150" height="1280"/>
      <rect x="-40" y="380" width="200" height="520"/>
      <rect x="640" y="-40" width="150" height="1280"/>
      <rect x="600" y="-40" width="190" height="640"/>
      <rect x="-40" y="1100" width="830" height="140"/>
    </g>
  </svg>

  <p class="subtitle">家族の未来をひらく手引き</p>
  <h1 class="title">いつか、わが家にも<br>春は来るだろうか?</h1>

  <div class="author">
    <p class="author-role">婚活成幸シフトナビゲーター</p>
    <p class="author-name">結 はる<small>(むすび はる)</small></p>
  </div>

  <p class="message">お子さんの結婚問題で<br>悩んでいるということは、<br>今こそお子さんと<br>悩みを共有し対話を重ね、<br>親子の絆を深める絶好の<br>機会なんだと<br>思いませんか。</p>

  <div class="gift">
    <span class="gift-label">読者プレゼント</span>
    <div class="gift-body">運命の人に<br>出会う方法を<br>診断</div>
  </div>
</div>
</body>
</html>
```